Training Company Needs a Web Design

We are a Training company that needs a website design completed for us. "The Harbor Loft" The website will be a 'community space' specialising in 'Change and Transformation'. It will be a 'space' where individuals can come to find out 'latest news', upcoming events and courses, chat with others and find 'tools and templates'. They will need to login as a 'Member'.

The final design needs to be professional but have a 'fun and interactive' feel and appeal to our target audience who are predominantly corporate individuals.

Target Market(s)

Corporate Individuals - they may have a Change or Project background

Industry/Entity Type

Business Consultant

Number of Pages Required

3 page

Font styles to use
Sans Serif

Requirements
Must have
• Design for 'Home Page'
• A professional and corporate 'feel' but be fun and interactive.
Nice to have
• A 'sense' of how some of the other pages may be designed or laid out.

```html
<!DOCTYPE html>
<html lang="en">
<head>
<meta charset="utf-8">
<title>The Harbor Loft — Home</title>
<link href="https://fonts.googleapis.com/css2?family=Lato:wght@300;400;700;900&display=swap" rel="stylesheet">
<style>
:root{
  --stage:#6f7fd6;
  --blue:#1a9ad6;
  --blue-deep:#2a56f0;
  --green:#9bcc3c;
  --purple:#9b59c7;
  --lavender:#e3e4f8;
  --ink:#444b55;
  --muted:#8a9099;
  --line:#d9dde3;
  --navy:#0d4f8f;
  --navy-dark:#083a6b;
  --white:#ffffff;
}
*{box-sizing:border-box;margin:0;padding:0}
html,body{width:1200px;height:1000px;overflow:hidden}
body{background:var(--stage);font-family:"Lato",sans-serif;color:var(--ink);position:relative}
.page{position:absolute;left:429px;top:0;width:1200px;height:3500px;background:var(--white);transform:scale(.2857);transform-origin:top left;box-shadow:0 0 40px rgba(0,0,0,.25);overflow:hidden}
.page > section,.page > header,.page > footer{overflow:hidden}
.wrap{width:780px;margin:0 auto;position:relative}
h2.section-title{color:var(--blue);font-size:30px;font-weight:700;margin-bottom:12px;line-height:1.2}
p.lead{font-size:14px;line-height:1.6;color:var(--muted)}
.rule{height:3px;background:var(--blue);margin-top:24px}
.btn{display:inline-block;border-radius:20px;padding:8px 24px;font-size:14px;font-weight:700;white-space:nowrap}

/* header */
.site-header{height:150px;display:flex;align-items:center;justify-content:space-between;padding:0 210px}
.brand{display:flex;align-items:center;gap:12px;color:var(--blue);font-weight:700;font-size:22px;white-space:nowrap}
.brand-square{width:64px;height:64px;background:var(--blue);flex:none}
.nav{display:flex;align-items:center;gap:20px;font-size:16px;color:var(--blue);font-weight:700;letter-spacing:.5px;white-space:nowrap}
.cart{position:relative;display:flex}
.cart .badge{position:absolute;top:-12px;right:-12px;width:20px;height:20px;border-radius:50%;background:var(--purple);color:#fff;font-size:11px;display:flex;align-items:center;justify-content:center}
.btn-signin{background:var(--blue);color:#fff}
.btn-signup{border:2px solid var(--purple);color:var(--purple)}

/* hero */
.hero{height:500px;position:relative;background:linear-gradient(100deg,var(--blue-deep) 0%,#3f88d8 35%,#7fbf4e 70%,var(--green) 100%);color:#fff}
.hero-copy{position:absolute;left:220px;top:52px;width:640px}
.hero h1{font-size:68px;font-weight:900;line-height:.95}
.hero .tagline{font-size:20px;font-weight:700;margin-top:12px;line-height:1.2}
.hero p{font-size:14px;line-height:1.6;margin-top:22px;opacity:.9;width:560px}
.btn-view{border:2px solid #fff;color:#fff;margin-top:22px;font-size:13px;padding:6px 24px}
.dots{position:absolute;left:0;right:0;bottom:18px;display:flex;justify-content:center;gap:10px}
.dots i{width:9px;height:9px;border-radius:50%;background:rgba(255,255,255,.6)}
.dots i:first-child{background:#fff}

/* welcome */
.welcome{height:460px;padding-top:34px}
.features{display:grid;grid-template-columns:repeat(3,1fr);gap:26px 40px;margin-top:22px}
.feature h3{display:flex;align-items:center;gap:12px;font-size:17px;font-weight:700;color:var(--ink);margin-bottom:8px}
.feature p{font-size:12px;line-height:1.55;color:var(--muted)}
.feature svg{width:22px;height:22px;fill:var(--blue);flex:none}

/* courses */
.courses{height:510px;padding-top:26px}
.courses-head{display:flex;justify-content:space-between;align-items:flex-end}
.courses-head p{width:380px;font-size:13px;color:var(--muted);line-height:1.5}
.filters{width:340px;display:flex;flex-wrap:wrap;gap:8px 20px;font-size:12px;font-weight:700;color:var(--ink);padding-bottom:2px}
.filters .on{color:var(--purple);border-bottom:2px solid var(--purple)}
.tiles{display:grid;grid-template-columns:repeat(4,1fr);grid-template-rows:repeat(3,122px);margin-top:20px}
.tile{display:flex;align-items:center;justify-content:center;color:#fff;font-size:15px;font-weight:700;letter-spacing:1px}
.t-design{grid-row:1/3;background:linear-gradient(135deg,#e8502a,#c42c50)}
.t-photo{grid-row:1/3;background:linear-gradient(135deg,#1f9fd4,#1d3c7a)}
.t-edu{background:linear-gradient(135deg,#2bb8a8,#1c5e79)}
.t-anim{background:var(--purple);flex-direction:column;gap:8px;padding:14px;text-align:center}
.t-anim span{font-size:10px;font-weight:400;line-height:1.4;letter-spacing:0}
.t-video{background:linear-gradient(135deg,#8a8f96,#2e3238)}
.t-audio{grid-row:2/4;background:linear-gradient(135deg,#2b6fd1,#102140)}
.t-web{background:linear-gradient(135deg,#c8d43a,#3e8a5a)}
.t-dev{background:linear-gradient(135deg,#263b6a,#0b1020)}
.t-it{background:linear-gradient(135deg,#9b59c7,#4a1f7a)}

/* band */
.band{height:250px;background:var(--lavender);display:flex;align-items:center}
.band .wrap{display:flex;justify-content:space-between}
.perk{width:170px;text-align:center}
.perk .circle{width:60px;height:60px;border-radius:50%;background:var(--purple);margin:0 auto 18px;display:flex;align-items:center;justify-content:center}
.perk svg{width:26px;height:26px;fill:none;stroke:#fff;stroke-width:2}
.perk h4{font-size:12px;font-weight:700;margin-bottom:8px}
.perk p{font-size:11px;line-height:1.5;color:var(--muted)}

/* blog */
.blog{height:400px;padding-top:40px}
.posts{display:grid;grid-template-columns:repeat(4,1fr);gap:20px;margin-top:20px}
.post-img{height:110px}
.post h4{font-size:12px;text-align:center;margin:12px 0 6px}
.post .meta{font-size:10px;text-align:center;color:var(--muted)}
.post p{font-size:10px;line-height:1.5;color:var(--muted);text-align:center;margin-top:8px}

/* testimonials */
.testimonials{height:360px;padding-top:20px}
.quotes{display:grid;grid-template-columns:1fr 1fr;gap:28px 40px;margin-top:20px}
.quote{display:flex;gap:18px}
.avatar{width:68px;height:68px;border-radius:50%;flex:none;border:3px solid var(--purple)}
.quote h5{color:var(--blue);font-size:13px}
.quote .role{font-size:11px;color:var(--muted);margin:2px 0 6px}
.quote p{font-size:11px;line-height:1.5;color:var(--muted)}
.testimonials .dots{position:static;margin-top:26px}
.testimonials .dots i{background:var(--line)}
.testimonials .dots i:first-child{background:var(--purple)}

/* partners */
.partners{height:100px;border-bottom:3px solid var(--blue)}
.partners .wrap{display:flex;align-items:center;justify-content:space-between;height:100%}
.arrow{width:24px;height:24px;border-radius:50%;border:1px solid var(--muted);color:var(--muted);font-size:14px;display:flex;align-items:center;justify-content:center}
.partner{width:110px;height:34px;background:#c9cdd3;border-radius:4px}

/* contact */
.contact{height:470px;padding-top:32px}
.contact-grid{display:flex;justify-content:space-between;margin-top:10px}
.contact-info{width:380px;font-size:12px;color:var(--muted);line-height:1.5}
.contact-info ul{margin-top:12px}
.contact-info li{list-style:none;display:flex;align-items:center;gap:8px;margin-bottom:5px}
.contact-info li svg{width:12px;height:12px;fill:var(--blue);flex:none}
.form{margin-top:14px}
.form .row{display:flex;gap:12px;margin-bottom:9px}
.field{flex:1;height:28px;border:1px solid var(--line);font-size:11px;padding:6px 10px;color:var(--muted)}
.field.tall{height:62px}
.btn-send{border:2px solid var(--blue);color:var(--blue);font-size:11px;padding:5px 22px;margin-top:4px}
.map{width:360px;height:360px;background:linear-gradient(135deg,#efe8d2,#dfe6cd)}

/* footer */
.site-footer{height:300px;background:var(--navy);color:#d8e4f2}
.footer-cols{height:230px;display:flex;justify-content:space-between;padding-top:34px}
.footer-cols h6{font-size:12px;color:#fff;margin-bottom:14px}
.footer-cols p,.footer-cols li{font-size:10px;line-height:1.6;list-style:none}
.footer-cols .col{width:170px}
.socials{display:flex;gap:6px;margin-top:14px}
.socials i{width:14px;height:14px;background:#fff}
.subscribe-field{height:24px;background:#fff;margin:10px 0}
.btn-sub{border:1px solid #fff;color:#fff;font-size:10px;padding:4px 16px}
.footer-bottom{height:70px;background:var(--navy-dark);display:flex;align-items:center;justify-content:center;font-size:11px}
</style>
</head>
<body>
<div class="page">

  <header class="site-header">
    <div class="brand"><span class="brand-square"></span>The Harbor Loft</div>
    <nav class="nav">
      <span>ABOUT</span><span>COURSES</span><span>BLOG</span><span>CONTACT</span>
      <span class="cart"><svg width="26" height="22" viewBox="0 0 26 22" fill="none" stroke="#8a9099" stroke-width="2"><path d="M1 2h4l3 12h13l3-9H7"/><circle cx="10" cy="19" r="2"/><circle cx="19" cy="19" r="2"/></svg><span class="badge">0</span></span>
      <svg width="22" height="22" viewBox="0 0 24 24" fill="none" stroke="#444b55" stroke-width="3"><circle cx="10" cy="10" r="7"/><path d="M15 15l7 7"/></svg>
      <span class="btn btn-signin">SIGN IN</span>
      <span class="btn btn-signup">SIGN UP</span>
    </nav>
  </header>

  <section class="hero" role="img" aria-label="Photo of a workshop class with people at desks, tinted blue to green">
    <div class="hero-copy">
      <h1>THE<br>HARBOR<br>LOFT</h1>
      <div class="tagline">LOREM IPSUM DOLOR SIT AMET, CONSECTETUR ADIPISCING ELIT</div>
      <p>Nam auctor arcu ut efficitur blandit. Ut posuere dolor nunc, vitae eleifend nisl sodales in. Suspendisse varius sapien sed condimentum. Nam a felis nec libero vestibulum convallis sit amet sed lectus dictum erat in massa.</p>
      <span class="btn btn-view">VIEW MORE</span>
    </div>
    <div class="dots"><i></i><i></i><i></i><i></i><i></i></div>
  </section>

  <section class="welcome">
    <div class="wrap">
      <h2 class="section-title">Welcome to The Harbor Loft</h2>
      <p class="lead">A community space for everyone working through change and transformation, with news, events, courses and tools in one place.</p>
      <p class="lead">Members can join live sessions, chat with peers, download templates and follow the latest thinking on leading change inside large organisations today.</p>
      <div class="features">
        <div class="feature"><h3><svg viewBox="0 0 24 24"><circle cx="8" cy="14" r="6"/><circle cx="18" cy="6" r="4"/></svg>CUSTOM COURSES</h3><p>Ut porttitor quam nec risus ultricies efficitur. Pellentesque sagittis sed magna a mollis integer consectetur tortor feugiat.</p></div>
        <div class="feature"><h3><svg viewBox="0 0 24 24"><path d="M3 21l4-1L20 7l-3-3L4 17z"/></svg>2. LOREM IPSUM</h3><p>Ut porttitor quam nec risus ultricies efficitur. Pellentesque sagittis sed magna a mollis integer consectetur tortor feugiat.</p></div>
        <div class="feature"><h3><svg viewBox="0 0 24 24"><path d="M12 2l3 7h7l-6 4 2 8-6-5-6 5 2-8-6-4h7z"/></svg>3. LOREM IPSUM</h3><p>Ut porttitor quam nec risus ultricies efficitur. Pellentesque sagittis sed magna a mollis integer consectetur tortor feugiat.</p></div>
        <div class="feature"><h3><svg viewBox="0 0 24 24"><path d="M4 20l6-6M10 8l6 6 4-10z"/></svg>4. LOREM IPSUM</h3><p>Ut porttitor quam nec risus ultricies efficitur. Pellentesque sagittis sed magna a mollis integer consectetur tortor feugiat.</p></div>
        <div class="feature"><h3><svg viewBox="0 0 24 24"><circle cx="12" cy="12" r="10"/></svg>5. LOREM IPSUM</h3><p>Ut porttitor quam nec risus ultricies efficitur. Pellentesque sagittis sed magna a mollis integer consectetur tortor feugiat.</p></div>
        <div class="feature"><h3><svg viewBox="0 0 24 24"><path d="M12 21L3 12a5 5 0 019-6 5 5 0 019 6z"/></svg>6. LOREM IPSUM</h3><p>Ut porttitor quam nec risus ultricies efficitur. Pellentesque sagittis sed magna a mollis integer consectetur tortor feugiat.</p></div>
      </div>
      <div class="rule"></div>
    </div>
  </section>

  <section class="courses">
    <div class="wrap">
      <div class="courses-head">
        <div>
          <h2 class="section-title">Discover our range of courses</h2>
          <p>More than 15,000 videos in more than 900 courses await you in the main library. Pick a topic and get started.</p>
        </div>
        <div class="filters"><span class="on">ALL</span><span>DESIGN</span><span>WEB</span><span>PHOTOGRAPHY</span><span>BUSINESS</span><span>EDUCATION</span><span>3D+ANIMATION</span><span>VIDEO</span><span>AUDIO+MUSIC</span></div>
      </div>
      <div class="tiles">
        <div class="tile t-design" role="img" aria-label="Design course photo">DESIGN</div>
        <div class="tile t-photo" role="img" aria-label="Photography course photo">PHOTOGRAPHY</div>
        <div class="tile t-edu" role="img" aria-label="Education course photo">EDUCATION</div>
        <div class="tile t-anim">3D + ANIMATION<span>Learn modelling, motion and rendering with step by step projects from working studio artists.</span></div>
        <div class="tile t-video" role="img" aria-label="Video course photo">VIDEO</div>
        <div class="tile t-audio" role="img" aria-label="Audio and music course photo">AUDIO + MUSIC</div>
        <div class="tile t-web" role="img" aria-label="Web course photo">WEB</div>
        <div class="tile t-dev" role="img" aria-label="Developer course photo">DEVELOPER</div>
        <div class="tile t-it" role="img" aria-label="IT course photo">IT</div>
      </div>
    </div>
  </section>

  <section class="band">
    <div class="wrap">
      <div class="perk"><div class="circle"><svg viewBox="0 0 24 24"><rect x="4" y="5" width="16" height="11"/><path d="M2 19h20"/></svg></div><h4>RESPONSIVE MOBILE READY COURSES</h4><p>Study on any device and pick up right where you left off.</p></div>
      <div class="perk"><div class="circle"><svg viewBox="0 0 24 24"><path d="M2 12s4-7 10-7 10 7 10 7-4 7-10 7S2 12 2 12z"/><circle cx="12" cy="12" r="3"/></svg></div><h4>LIVE ON-LINE LEARNING</h4><p>Join scheduled sessions and ask questions to the tutor live.</p></div>
      <div class="perk"><div class="circle"><svg viewBox="0 0 24 24"><circle cx="12" cy="12" r="4"/><path d="M12 2v4M12 18v4M2 12h4M18 12h4M5 5l3 3M16 16l3 3M5 19l3-3M16 8l3-3"/></svg></div><h4>LOREM IPSUM</h4><p>Tools and templates ready to use in your next change project.</p></div>
      <div class="perk"><div class="circle"><svg viewBox="0 0 24 24"><path d="M12 3l3 6 6 1-4 4 1 6-6-3-6 3 1-6-4-4 6-1z"/></svg></div><h4>LOREM IPSUM</h4><p>Earn member badges as you complete courses and events.</p></div>
    </div>
  </section>

  <section class="blog">
    <div class="wrap">
      <h2 class="section-title">Latest Blog Posts</h2>
      <p class="lead">Fresh thinking, stories and practical advice from our community of change leaders.</p>
      <div class="posts">
        <div class="post"><div class="post-img" role="img" aria-label="Blog photo of people at a laptop" style="background:linear-gradient(135deg,#9fb8cf,#55708a)"></div><h4>SAMPLE BLOG POST</h4><div class="meta">June 12, 2016 · 3 comments</div><p>Curabitur quam ex, varius et dapibus ut, tincidunt sit amet nisl. Donec ac dui at mauris tempus.</p></div>
        <div class="post"><div class="post-img" role="img" aria-label="Blog photo of a web code graphic" style="background:linear-gradient(135deg,#3a3a3a,#e0562b)"></div><h4>SIMPLE BLOG POST</h4><div class="meta">June 10, 2016 · 5 comments</div><p>Curabitur quam ex, varius et dapibus ut, tincidunt sit amet nisl. Donec ac dui at mauris tempus.</p></div>
        <div class="post"><div class="post-img" role="img" aria-label="Blog photo of a woman at a desk" style="background:linear-gradient(135deg,#e8e2d8,#9aa7b6)"></div><h4>SIMPLE BLOG POST</h4><div class="meta">June 08, 2016 · 2 comments</div><p>Curabitur quam ex, varius et dapibus ut, tincidunt sit amet nisl. Donec ac dui at mauris tempus.</p></div>
        <div class="post"><div class="post-img" role="img" aria-label="Blog photo of a video editing screen" style="background:linear-gradient(135deg,#2c6fa8,#132a44)"></div><h4>SIMPLE BLOG POST</h4><div class="meta">June 05, 2016 · 4 comments</div><p>Curabitur quam ex, varius et dapibus ut, tincidunt sit amet nisl. Donec ac dui at mauris tempus.</p></div>
      </div>
    </div>
  </section>

  <section class="testimonials">
    <div class="wrap">
      <h2 class="section-title">Testimonials</h2>
      <p class="lead">What our members say about learning and growing with the community.</p>
      <div class="quotes">
        <div class="quote"><div class="avatar" role="img" aria-label="Member portrait" style="background:#c9b3a4"></div><div><h5>ANNA WEBSTER</h5><div class="role">Project Lead</div><p>Curabitur quam ex, varius et dapibus ut, tincidunt sit amet nisl. Donec ac dui at mauris tempus pretium sed in felis.</p></div></div>
        <div class="quote"><div class="avatar" role="img" aria-label="Member portrait" style="background:#b8a08a"></div><div><h5>TOM REILLY</h5><div class="role">Change Manager</div><p>Curabitur quam ex, varius et dapibus ut, tincidunt sit amet nisl. Donec ac dui at mauris tempus pretium sed in felis.</p></div></div>
        <div class="quote"><div class="avatar" role="img" aria-label="Member portrait" style="background:#d4b89c"></div><div><h5>GRACE LINTON</h5><div class="role">Programme Director</div><p>Curabitur quam ex, varius et dapibus ut, tincidunt sit amet nisl. Donec ac dui at mauris tempus pretium sed in felis.</p></div></div>
        <div class="quote"><div class="avatar" role="img" aria-label="Member portrait" style="background:#a89a8c"></div><div><h5>NICK HALE</h5><div class="role">Business Analyst</div><p>Curabitur quam ex, varius et dapibus ut, tincidunt sit amet nisl. Donec ac dui at mauris tempus pretium sed in felis.</p></div></div>
      </div>
      <div class="dots"><i></i><i></i><i></i><i></i><i></i></div>
    </div>
  </section>

  <section class="partners">
    <div class="wrap">
      <span class="arrow">‹</span>
      <span class="partner"></span><span class="partner"></span><span class="partner"></span><span class="partner"></span><span class="partner"></span>
      <span class="arrow">›</span>
    </div>
  </section>

  <section class="contact">
    <div class="wrap">
      <h2 class="section-title">Contact Us</h2>
      <div class="contact-grid">
        <div class="contact-info">
          <p>Drop us a line and a member of the team will reply within one working day.</p>
          <ul>
            <li><svg viewBox="0 0 12 12"><path d="M6 0a4 4 0 014 4c0 3-4 8-4 8S2 7 2 4a4 4 0 014-4z"/></svg>14 Quay Lane, Portside</li>
            <li><svg viewBox="0 0 12 12"><path d="M2 0h3l1 3-2 1a7 7 0 004 4l1-2 3 1v3c0 1-1 2-2 2A10 10 0 010 2c0-1 1-2 2-2z"/></svg>555 0142 880</li>
            <li><svg viewBox="0 0 12 12"><path d="M0 2h12v8H0zM0 2l6 4 6-4" fill="none" stroke="#1a9ad6"/></svg>hello@harborloft.example</li>
          </ul>
          <div class="form">
            <p style="margin-bottom:8px">Send us a message:</p>
            <div class="row"><div class="field">First name</div><div class="field">Last name</div></div>
            <div class="row"><div class="field">Email</div></div>
            <div class="row"><div class="field">Subject</div></div>
            <div class="row"><div class="field tall">Message</div></div>
            <span class="btn btn-send">SEND</span>
          </div>
        </div>
        <div class="map" role="img" aria-label="Street map showing the office location"></div>
      </div>
    </div>
  </section>

  <footer class="site-footer">
    <div class="wrap footer-cols">
      <div class="col"><h6>ABOUT US</h6><p>A community space for change and transformation, where members share news, events, courses and practical tools with each other.</p><div class="socials"><i></i><i></i><i></i><i></i></div></div>
      <div class="col"><h6>NAVIGATION</h6><ul><li>About</li><li>Courses</li><li>Blog</li><li>Contact</li></ul></div>
      <div class="col"><h6>LATEST POSTS</h6><ul><li>Leading through change</li><li>Project templates</li><li>Member stories</li><li>Upcoming events</li></ul></div>
      <div class="col"><h6>SUBSCRIBE</h6><p>Get the latest news and events in your inbox every month.</p><div class="subscribe-field"></div><span class="btn btn-sub">SUBSCRIBE</span></div>
    </div>
    <div class="footer-bottom">© The Harbor Loft 2016</div>
  </footer>

</div>
</body>
</html>
```